Web Design Front Page Only for Organic Skincare

We have been in business for nearly 20 years. We are run by all females and sell anything from aromatherapy, skincare and pharmacy types products to health food shops and pharmacy. We are looking for an attractive and colourful but simple front web page design for our wholesale customers to look at. We want our customers to start using our website to find information rather than ringing us. So we want it to be attractive to our buyers who are young and funky.
Updates

To give you an idea of the products we sell to pharmacy and health food shops also beauty shops and hair salons.  We mainly deal with organic body and skincare, aromatherapy oils and body products, but also do some simple pharmacy products such as bandages and pill boxes, finger splits, walking frames and wheelchairs.  We are only looking for the front page of the website.  The back-end will be done in-house.  We currently do not have a logo designed so I am thinking that once we have done the website design we can build a logo from it.  I like bright colours and want something that is inviting to further discover that we do many different types of products.

Target Market(s)

young girls who are our retail buyers

Industry/Entity Type

Pharmacy

Requirements
Must have
• A section which says

Customer Log in
Should not have
• don't worry about too much writing or tabs. We will insert these later. Just come up with design image.

```html
<!DOCTYPE html>
<html lang="en">
<head>
<meta charset="utf-8">
<title>Verdella Healthcare</title>
<link href="https://fonts.googleapis.com/css2?family=Raleway:wght@400&family=Roboto+Condensed:wght@700&family=Lato:wght@300;400&display=swap" rel="stylesheet">
<style>
  :root {
    --green-deep: #0c850c;
    --green-top: #1a9a1a;
    --green-glow: #2dad2d;
    --green-bottom: #86dc80;
    --panel-green: #52b04d;
    --nav-active: #12880f;
    --product-bg: #b6f6b4;
    --btn-green: #47ad43;
    --footer-green: #3d9a3a;
    --text-white: #ffffff;
    --text-muted: #6f7a6f;
    --dot-line: rgba(255,255,255,0.75);
  }
  * { box-sizing: border-box; margin: 0; padding: 0; }
  html, body { width: 943px; height: 1200px; overflow: hidden; }
  body {
    position: relative;
    background:
      radial-gradient(ellipse 520px 200px at 330px 60px, var(--green-glow), transparent 70%),
      linear-gradient(to bottom, var(--green-top) 0px, var(--green-deep) 214px, var(--green-deep) 900px, var(--green-bottom) 1200px);
    font-family: "Lato", sans-serif;
  }
  .band-shadow {
    position: absolute; left: 0; top: 204px; width: 943px; height: 16px;
    background: linear-gradient(to bottom, rgba(0,60,0,0), rgba(0,60,0,0.35) 60%, rgba(0,60,0,0));
  }
  .brand {
    position: absolute; left: 130px; top: 70px;
    font-family: "Raleway", sans-serif; font-weight: 400;
    font-size: 33px; letter-spacing: 2.2px; color: var(--text-white);
    white-space: nowrap;
  }
  .account {
    position: absolute; left: 664px; top: 72px; width: 180px; height: 29px;
    display: flex; box-shadow: 0 2px 3px rgba(0,50,0,0.35);
  }
  .account a {
    flex: 1; display: flex; align-items: center; justify-content: center;
    background: linear-gradient(to bottom, #45b040, #2f9a2b);
    color: var(--text-white); font-size: 12px; text-decoration: none;
    border-right: 1px solid #7fcf7b;
  }
  .account a:last-child { border-right: none; }
  .main-nav {
    position: absolute; left: 129px; top: 157px; width: 716px; height: 57px;
    background: var(--panel-green); display: flex;
  }
  .main-nav a {
    position: relative; display: flex; align-items: center; justify-content: center;
    font-family: "Roboto Condensed", sans-serif; font-weight: 700; font-size: 15.5px;
    color: var(--text-white); text-decoration: none; height: 100%;
  }
  .main-nav a + a::before {
    content: ""; position: absolute; left: 0; top: 10px; bottom: 10px;
    border-left: 1px dotted rgba(255,255,255,0.5);
  }
  .main-nav a.active { background: var(--nav-active); }
  .main-nav a.active::before, .main-nav a.active + a::before { display: none; }
  .hero {
    position: absolute; left: 129px; top: 214px; width: 715px; height: 280px;
    display: flex; box-shadow: 0 12px 24px rgba(0,50,0,0.4);
  }
  .hero .leaf { width: 226px; background: linear-gradient(135deg, #b5e03a, #6fbf1c 50%, #3c8d10); }
  .hero .lavender { width: 237px; background: linear-gradient(to bottom, #4a3a4a, #6a4fb0 35%, #7a62c2 60%, #5d8a3a); }
  .hero .grass { width: 252px; background: linear-gradient(120deg, #1f4d1a, #3f8a28 45%, #214d1c); }
  .category-menu {
    position: absolute; left: 129px; top: 518px; width: 228px; height: 311px;
    background: var(--panel-green); padding: 7px 13px 0;
    list-style: none;
  }
  .category-menu li {
    height: 43px; display: flex; align-items: center; justify-content: center;
    font-family: "Roboto Condensed", sans-serif; font-weight: 700; font-size: 15px;
    color: var(--text-white); border-bottom: 1px dotted var(--dot-line);
  }
  .category-menu li:last-child { border-bottom: none; }
  .products {
    position: absolute; left: 379px; top: 517px; width: 465px; height: 491px;
    background: var(--product-bg);
  }
  .products .row-divider {
    position: absolute; left: 12px; right: 11px; top: 251px;
    border-top: 1px dotted #6f8f6f;
  }
  .product { position: absolute; width: 200px; height: 230px; }
  .product .thumb {
    position: absolute; left: 36px; top: 0; width: 54px; height: 144px;
    background: linear-gradient(to bottom, #f4f4f4 0%, #e6e6e6 80%, #f0a040 88%, #e0e0e0 92%);
    border-radius: 4px 4px 10px 10px;
  }
  .product .name {
    position: absolute; left: 0; top: 159px;
    font-size: 12px; font-weight: 300; color: var(--text-muted); white-space: nowrap;
  }
  .product .price {
    position: absolute; left: 0; top: 178px;
    font-size: 12px; font-weight: 300; color: var(--text-muted);
  }
  .product .add-btn {
    position: absolute; left: 1px; top: 211px; width: 96px; height: 16px;
    background: var(--btn-green); color: var(--text-white);
    font-size: 12px; font-weight: 300; letter-spacing: 0.3px;
    display: flex; align-items: center; justify-content: center;
  }
  .footer-nav {
    position: absolute; left: 138px; top: 1124px; width: 668px; height: 49px;
    background: var(--footer-green);
    display: flex; align-items: center; justify-content: center;
    font-size: 8.5px; color: var(--text-white);
  }
  .footer-nav a { color: var(--text-white); text-decoration: none; }
  .footer-nav span { margin: 0 8px; }
</style>
</head>
<body>
  <div class="band-shadow"></div>

  <div class="brand">VERDELLA HEALTHCARE</div>

  <nav class="account" aria-label="Customer log in">
    <a href="#">Log in</a>
    <a href="#">Register</a>
  </nav>

  <nav class="main-nav">
    <a href="#" style="width:117px">ABOUT US</a>
    <a href="#" style="width:121px">HEALTH FOOD</a>
    <a href="#" class="active" style="width:105px">PHARMACY</a>
    <a href="#" style="width:134px">SUPERMARKET</a>
    <a href="#" style="width:98px">BEAUTY</a>
    <a href="#" style="width:141px">CONTACT US</a>
  </nav>

  <section class="hero">
    <div class="leaf" role="img" aria-label="Close-up photo of a bright green leaf"></div>
    <div class="lavender" role="img" aria-label="Photo of purple lavender flowers in bloom"></div>
    <div class="grass" role="img" aria-label="Photo of grass blades with dew drops"></div>
  </section>

  <ul class="category-menu">
    <li>FACE CARE</li>
    <li>HAIR CARE</li>
    <li>FRAGRANCE</li>
    <li>BATH &amp; BODY</li>
    <li>FACE CARE</li>
    <li>HAIR CARE</li>
    <li>FRAGRANCE</li>
  </ul>

  <section class="products">
    <div class="product" style="left:45px; top:12px">
      <div class="thumb" role="img" aria-label="Photo of a white cream tube"></div>
      <div class="name">PRECIOUS CREAM 50 ML</div>
      <div class="price">70$</div>
      <div class="add-btn">ADD TO BAG</div>
    </div>
    <div class="product" style="left:268px; top:12px">
      <div class="thumb" role="img" aria-label="Photo of a white cream tube"></div>
      <div class="name">PRECIOUS CREAM 50 ML</div>
      <div class="price">70$</div>
      <div class="add-btn">ADD TO BAG</div>
    </div>
    <div class="row-divider"></div>
    <div class="product" style="left:44px; top:261px">
      <div class="thumb" role="img" aria-label="Photo of a white cream tube"></div>
      <div class="name">PRECIOUS CREAM 50 ML</div>
      <div class="price">70$</div>
      <div class="add-btn">ADD TO BAG</div>
    </div>
    <div class="product" style="left:265px; top:261px">
      <div class="thumb" role="img" aria-label="Photo of a white cream tube"></div>
      <div class="name">PRECIOUS CREAM 50 ML</div>
      <div class="price">70$</div>
      <div class="add-btn">ADD TO BAG</div>
    </div>
  </section>

  <footer class="footer-nav">
    <a href="#">About us</a><span>|</span>
    <a href="#">Health food</a><span>|</span>
    <a href="#">Pharmacy</a><span>|</span>
    <a href="#">Supermarket</a><span>|</span>
    <a href="#">Beauty</a><span>|</span>
    <a href="#">Contact us</a>
  </footer>
</body>
</html>
```